Kelvar Systems Website

Website design for our company: Kelvar Systems.
The website should look fresh and IT focused. Please have a look at http://www.kelvarsystems.net.au/ for our current design. We want something fresh and new, professional looking, in WordPress so we can easily make changes.

Industry/Entity Type

It Company

```html
<!DOCTYPE html>
<html lang="en">
<head>
<meta charset="utf-8">
<title>Kelvar Systems</title>
<link href="https://fonts.googleapis.com/css2?family=Open+Sans:wght@400;600;700&display=swap" rel="stylesheet">
<style>
:root{
  --green:#00b159;
  --green-dark:#009a4c;
  --ink:#333333;
  --text:#444444;
  --pale:#f2f2f2;
  --white:#ffffff;
  --button:#555555;
}
*{margin:0;padding:0;box-sizing:border-box}
html,body{width:851px;height:1200px;overflow:hidden}
body{position:relative;background:var(--white);font-family:"Open Sans",sans-serif;color:var(--text)}
.abs{position:absolute}
.top-band{left:0;top:0;width:851px;height:274px;background:var(--green)}
.intro-band{left:0;top:274px;width:851px;height:325px;background:var(--pale)}
.footer-band{left:0;top:954px;width:851px;height:246px;background:var(--pale)}
.search{left:603px;top:19px;width:154px;height:16px;background:var(--green-dark);color:#d9f3e5;font-size:8.5px;padding:2px 6px;line-height:12px}
.search svg{position:absolute;right:4px;top:3px}
.header{left:92px;top:41px;width:666px;height:64px;border-radius:4px;background:linear-gradient(#ffffff,#e8e8e8)}
.brand{left:9px;top:10px;display:flex;align-items:center;gap:6px;font-size:12px;font-weight:700;color:var(--green)}
.brand-dot{width:14px;height:14px;border-radius:50%;background:var(--green)}
.nav{left:172px;top:21px;display:flex;gap:0;font-size:9px;font-weight:700;color:var(--ink)}
.nav a{display:block;text-decoration:none;color:inherit;height:22px;line-height:22px;padding:0 9px}
.nav a.active{background:var(--green);color:var(--white);border-radius:2px;padding:0 16px;margin-right:1px}
.hero{left:92px;top:110px;width:666px;height:268px;background:radial-gradient(circle at 45% 40%,#a7adb6,#4f5660 60%,#2a2f38)}
.dots{left:401px;top:357px;display:flex;gap:3px}
.dots span{width:10px;height:10px;border-radius:50%;background:var(--white)}
.dots span:first-child{background:var(--green)}
.remote{left:92px;top:378px;width:666px;height:65px;background:var(--green);border-radius:0 0 8px 8px}
.remote-label{left:19px;top:23px;font-size:13.5px;font-weight:700;color:var(--white)}
.remote-input{left:130px;top:15px;width:416px;height:34px;background:var(--white);border-radius:3px;font-size:9.5px;color:#999;padding:0 7px;line-height:34px}
.remote-btn{left:556px;top:14px;width:98px;height:36px;background:var(--ink);border-radius:3px;color:var(--white);font-size:9.5px;font-weight:700;text-align:center;line-height:36px}
.welcome{left:80px;top:459px;width:691px;text-align:center}
h2{font-size:13px;font-weight:700;color:var(--ink);margin-bottom:8px}
.welcome p{font-size:8.8px;line-height:18.4px}
.welcome p+p{margin-top:18.4px}
.services-head{left:140px;top:635px;width:571px;text-align:center}
.services-head p{font-size:8.8px;margin-top:-2px}
.arrow{top:648px}
.service{top:718px;width:160px;text-align:center}
.service h3{font-size:10px;font-weight:700;color:var(--ink);margin-top:6px;height:32px}
.service p{font-size:9.6px;line-height:18.4px;font-weight:400;color:var(--text)}
.service .more{display:inline-block;margin-top:7px;background:var(--button);color:var(--white);font-size:10px;font-weight:700;padding:0 9px;height:21px;line-height:21px;border-radius:3px}
.service svg{display:block;margin:0 auto;height:32px}
.foot-col{top:974px;font-size:9.6px;line-height:21.3px;color:var(--text);list-style:none}
.contact{left:427px;top:974px;font-size:9.6px;line-height:17px}
.contact .gap{height:17px}
.social{left:604px;top:980px;display:flex;gap:10px}
.social span{width:24px;height:24px;border-radius:50%;background:var(--ink)}
.copyright{left:0;top:1160px;width:851px;text-align:center;font-size:9.6px}
</style>
</head>
<body>
<div class="abs top-band"></div>
<div class="abs intro-band"></div>
<div class="abs footer-band"></div>

<div class="abs search">Search
  <svg width="9" height="9" viewBox="0 0 9 9"><circle cx="3.5" cy="3.5" r="2.5" fill="none" stroke="#fff" stroke-width="1.3"/><line x1="5.3" y1="5.3" x2="8" y2="8" stroke="#fff" stroke-width="1.5"/></svg>
</div>

<header class="abs header">
  <div class="abs brand"><span class="brand-dot"></span>Kelvar Systems</div>
  <nav class="abs nav">
    <a class="active">HOME</a><a>CLIENTS</a><a>SERVICES</a><a>SUPPORTS</a><a>TESTIMONIALS</a><a>CONTACT US</a><a>ABOUT US</a>
  </nav>
</header>

<div class="abs hero" role="img" aria-label="Photo of a hand touching a glowing world map with network connection lines"></div>
<div class="abs dots"><span></span><span></span><span></span><span></span></div>

<section class="abs remote">
  <div class="abs remote-label">Remote Support</div>
  <div class="abs remote-input">Enter your 6-digit code</div>
  <div class="abs remote-btn">CONNECT NOW</div>
</section>

<section class="abs welcome">
  <h2>Welcome to Kelvar Systems</h2>
  <p>Kelvar Systems is an Adelaide based company with a single objective - to excel in the support and service of all computer and IT needs.<br>We provide a high level of consulting services using the most experienced engineers at a reasonable and fair price. We believe in using a Business Value<br>approach to every aspect of computer consulting to provide our clients with the most cost effective solutions.</p>
  <p>We strongly believe that we are in business with our clients. Each thing we do must be measured against our clients' business objectives. At the end of the day<br>our client's success is our success.</p>
</section>

<section class="abs services-head">
  <h2>Our Services</h2>
  <p>Kelvar Systems is an Adelaide based company with a single objective - to excel in the support and service of all computer and IT needs.</p>
</section>
<svg class="abs arrow" style="left:108px" width="12" height="20" viewBox="0 0 12 20"><polyline points="10,2 2,10 10,18" fill="none" stroke="#00b159" stroke-width="3"/></svg>
<svg class="abs arrow" style="left:732px" width="12" height="20" viewBox="0 0 12 20"><polyline points="2,2 10,10 2,18" fill="none" stroke="#00b159" stroke-width="3"/></svg>

<div class="abs service" style="left:89px">
  <svg viewBox="0 0 32 32" width="32"><rect x="2" y="9" width="28" height="20" rx="2" fill="#00b159"/><rect x="11" y="4" width="10" height="6" fill="none" stroke="#00b159" stroke-width="2"/><line x1="2" y1="18" x2="30" y2="18" stroke="#fff" stroke-width="1.5"/><rect x="9" y="16" width="3" height="5" fill="#fff"/><rect x="20" y="16" width="3" height="5" fill="#fff"/></svg>
  <h3>On-site Service</h3>
  <p>Lorem Ipsum is simply dummy text of the printing and typesetting industry. Lorem Ipsum has been the industry's standard dummy text ever since the 1500s</p>
  <span class="more">Read More</span>
</div>
<div class="abs service" style="left:261px">
  <svg viewBox="0 0 32 32" width="32"><path d="M6 10 A14 14 0 0 0 22 26 Z" fill="#00b159"/><rect x="6" y="24" width="8" height="5" fill="#00b159"/><line x1="14" y1="18" x2="22" y2="10" stroke="#00b159" stroke-width="2"/><path d="M20 4a8 8 0 0 1 8 8" fill="none" stroke="#00b159" stroke-width="2"/><path d="M20 8a4 4 0 0 1 4 4" fill="none" stroke="#00b159" stroke-width="2"/></svg>
  <h3>Remote Desktop Support</h3>
  <p>Lorem Ipsum is simply dummy text of the printing and typesetting industry. Lorem Ipsum has been the industry's standard dummy text ever since the 1500s</p>
  <span class="more">Read More</span>
</div>
<div class="abs service" style="left:431px">
  <svg viewBox="0 0 32 32" width="32"><rect x="2" y="9" width="28" height="20" rx="2" fill="#00b159"/><rect x="11" y="4" width="10" height="6" fill="none" stroke="#00b159" stroke-width="2"/><rect x="14" y="13" width="4" height="12" fill="#fff"/><rect x="10" y="17" width="12" height="4" fill="#fff"/></svg>
  <h3>Medical IT Service</h3>
  <p>Lorem Ipsum is simply dummy text of the printing and typesetting industry. Lorem Ipsum has been the industry's standard dummy text ever since the 1500s</p>
  <span class="more">Read More</span>
</div>
<div class="abs service" style="left:601px">
  <svg viewBox="0 0 32 32" width="32"><g transform="rotate(-45 16 16)"><rect x="4" y="11" width="24" height="10" rx="5" fill="none" stroke="#00b159" stroke-width="2.5"/><path d="M16 11h7a5 5 0 0 1 0 10h-7z" fill="#00b159"/></g></svg>
  <h3>Pharmacy IT Service</h3>
  <p>Lorem Ipsum is simply dummy text of the printing and typesetting industry. Lorem Ipsum has been the industry's standard dummy text ever since the 1500s</p>
  <span class="more">Read More</span>
</div>

<ul class="abs foot-col" style="left:118px">
  <li>Home</li><li>Clients</li><li>Services</li><li>Supports</li><li>Testimonials</li><li>Contact Us</li><li>About Us</li>
</ul>
<ul class="abs foot-col" style="left:254px">
  <li>On-site Service</li><li>Remote Desktop Support</li><li>Medical IT Service</li><li>Pharmacy IT Service</li><li>Website Design</li><li>Disaster Recovery</li><li>Hardware/ Software supply</li><li>Consumables</li>
</ul>
<address class="abs contact" style="font-style:normal">
  27 Harbour Lane<br>Seaview North &nbsp;&nbsp;&nbsp;5099<br>Australia
  <div class="gap"></div>
  Phone: &nbsp;&nbsp;0881234567<br>Fax: &nbsp;&nbsp;&nbsp;&nbsp;&nbsp;&nbsp;&nbsp;087654 3210<br>Mobile: &nbsp;0881234567
</address>
<div class="abs social" aria-label="Social links"><span></span><span></span><span></span><span></span><span></span></div>

<div class="abs copyright">© 2013 Company &nbsp;Name ,All Rights Reserved</div>
</body>
</html>
```